Business Card Design

Hoping for a black background business card, minimalistic design.
With the Marble Crest logo you created in white.

I would like to include:
My Name and title
Address (street address)
Reception: (phone number)
Fax: (fax number)
Reception: (email address)
Direct email: (email address)
Instagram: (ig handle)

```html
<!DOCTYPE html>
<html lang="en">
<head>
<meta charset="utf-8">
<title>Marble Crest – Business Card</title>
<link href="https://fonts.googleapis.com/css2?family=Open+Sans:wght@300;400;600&display=swap" rel="stylesheet">
<style>
  :root {
    --backdrop: #ebebeb;
    --card-black: #0f0f0f;
    --ink-white: #f2f2f2;
    --ink-soft: #d6d6d6;
    --rule: #bdbdbd;
  }
  * { margin: 0; padding: 0; box-sizing: border-box; }
  html, body {
    width: 1200px;
    height: 720px;
    overflow: hidden;
    background: var(--backdrop);
    font-family: "Open Sans", sans-serif;
  }
  .canvas {
    position: relative;
    width: 1200px;
    height: 720px;
  }
  .card {
    position: absolute;
    top: 192px;
    width: 520px;
    height: 336px;
    background: var(--card-black);
    color: var(--ink-white);
  }
  .card--info { left: 50px; }
  .card--brand { left: 630px; }

  /* Info side */
  .brand-block {
    position: absolute;
    left: 34px;
    top: 78px;
    width: 170px;
    display: flex;
    flex-direction: column;
    align-items: center;
    gap: 14px;
  }
  .brand-block .ring {
    width: 150px;
    height: 150px;
    border: 5px solid var(--ink-white);
    border-radius: 50%;
  }
  .brand-block .brand-name {
    font-weight: 400;
    font-size: 13px;
    letter-spacing: 3px;
    text-transform: uppercase;
  }
  .person {
    position: absolute;
    left: 262px;
    top: 44px;
  }
  .person .name {
    font-weight: 300;
    font-size: 26px;
    letter-spacing: 0.5px;
    text-transform: uppercase;
    line-height: 1.05;
  }
  .person .role {
    font-weight: 300;
    font-size: 12px;
    letter-spacing: 0.5px;
    text-transform: uppercase;
    color: var(--ink-soft);
  }
  .contact {
    position: absolute;
    left: 262px;
    top: 132px;
    display: grid;
    grid-template-columns: 82px auto;
    row-gap: 3px;
    font-size: 12.5px;
    line-height: 1.35;
  }
  .contact dt { font-weight: 600; }
  .contact dd { font-weight: 400; color: var(--ink-soft); }
  .contact .spacer { height: 10px; grid-column: 1 / -1; }

  /* Brand side */
  .lockup {
    position: absolute;
    left: 96px;
    top: 128px;
    display: flex;
    align-items: center;
    gap: 18px;
  }
  .lockup .ring {
    width: 74px;
    height: 74px;
    border: 4px solid var(--ink-white);
    border-radius: 50%;
  }
  .lockup .divider {
    width: 1.5px;
    height: 80px;
    background: var(--rule);
  }
  .lockup .brand-name {
    font-weight: 400;
    font-size: 30px;
    letter-spacing: 4px;
    text-transform: uppercase;
  }
</style>
</head>
<body>
<main class="canvas">
  <section class="card card--info">
    <div class="brand-block">
      <div class="ring"></div>
      <span class="brand-name">Marble Crest</span>
    </div>
    <div class="person">
      <p class="name">Alan Mercer</p>
      <p class="role">Director</p>
    </div>
    <dl class="contact">
      <dt>Address</dt><dd>Lindenweg 14<br>20XXX Hamburg</dd>
      <div class="spacer"></div>
      <dt>Mobile</dt><dd>040 111 47 302</dd>
      <dt>Fax</dt><dd>040 111 47 300</dd>
      <dt>Email</dt><dd>hello@marblecrest.com</dd>
      <dt>instagram</dt><dd>@marble.crest</dd>
    </dl>
  </section>

  <section class="card card--brand">
    <div class="lockup">
      <div class="ring"></div>
      <div class="divider"></div>
      <span class="brand-name">Marble Crest</span>
    </div>
  </section>
</main>
</body>
</html>
```